Current website re-design to a updated look and feel.

We currently have a website www.brightlanefreight.com that we want to give an updated look and feel to. We are a logistics company that competes with Harbex, Dm Whitfield, Tarn but on a smaller scale. We want something fresh and updated. We have two locations one in downtown Chicago, IL and one in Palatine IL. We are a fun group that also gets the job done. We know we need pictures of both locations and possibly a video, but we need fresh design ideas. The 'who we are' page is really the only page that we currently want to keep. The 'what we do' page needs to be completely re-done from a look and feel for sure.

Target Market(s)

Anyone who uses Truck transportation to move their product. Mainly US manufacturers.

Industry/Entity Type

Logistics

Number of Pages Required

5+ page

Font styles to use
Sans Serif

Colors
5c91c4
0355a3
d0dfed

Requirements
Must have
• The new design must entice people to want to do business with us. The design must have locations for pictures and at least one video which we know we will have to provide. Design must be easy to navigate.

```html
<!DOCTYPE html>
<html lang="en">
<head>
<meta charset="utf-8">
<title>Brightlane Freight — Relax, We Got This</title>
<link rel="stylesheet" href="https://fonts.googleapis.com/css2?family=Open+Sans:wght@400;600;700&family=Libre+Baskerville:wght@400;700&display=swap">
<style>
:root{
  --blue:#0355a3;
  --blue-mid:#5c91c4;
  --blue-pale:#d0dfed;
  --ink:#1e1e1e;
  --muted:#555;
  --grey-band:#efefef;
  --contact-bg:#f7f8fb;
  --login:#3d3d3d;
  --white:#fff;
  --sans:'Open Sans',Arial,sans-serif;
  --serif:'Libre Baskerville',Georgia,serif;
}
*{box-sizing:border-box;margin:0;padding:0}
html,body{width:1200px;height:4072px;overflow:hidden}
body{position:relative;font-family:var(--sans);color:var(--ink);background:var(--white)}
.abs{position:absolute}
a{color:inherit;text-decoration:none}

/* top bar */
.topbar{left:0;top:0;width:1200px;height:38px;background:var(--blue);color:var(--white);font-size:14px}
.topbar .tagline{position:absolute;left:66px;top:10px}
.topbar .phone{position:absolute;left:885px;top:8px;font-size:19px;font-weight:600;display:flex;align-items:center;gap:8px}
.topbar .socials{position:absolute;left:1060px;top:12px;display:flex;gap:24px}
.dot{width:14px;height:14px;border-radius:50%;background:var(--white);display:block}

/* nav */
.nav{left:0;top:38px;width:1200px;height:100px;background:var(--white)}
.brand{position:absolute;left:62px;top:26px;display:flex;align-items:center;gap:10px;font-family:var(--sans);font-weight:700;font-size:34px;color:var(--blue)}
.brand .sq{width:14px;height:14px;background:var(--blue)}
.nav ul{position:absolute;left:361px;top:40px;list-style:none;display:flex;gap:26px;font-size:16px;color:#333}
.login{position:absolute;left:988px;top:0;width:212px;height:100px;background:var(--login);color:var(--white);font-size:18px;display:flex;align-items:center;justify-content:center;letter-spacing:1px}

/* hero */
.hero{left:0;top:138px;width:1200px;height:522px;background:linear-gradient(160deg,#3b4f63 0%,#7a5a4a 40%,#b05a3e 60%,#2e3c4c 100%)}
.hero .eyebrow{position:absolute;width:100%;top:158px;text-align:center;color:var(--white);font-size:14px;letter-spacing:2px}
.hero h1{position:absolute;width:100%;top:190px;text-align:center;color:var(--white);font-family:var(--serif);font-size:50px;font-weight:700}
.btn{display:flex;align-items:center;justify-content:center;background:var(--blue);color:var(--white);font-size:15px;letter-spacing:1px}
.hero .btn{position:absolute;left:489px;top:292px;width:225px;height:50px}

.feature-band{left:0;top:660px;width:1200px;height:268px;background:var(--grey-band)}
.feature-card{width:248px;height:234px;top:624px;background:var(--white);border:4px solid var(--white);box-shadow:0 2px 8px rgba(0,0,0,.15);overflow:hidden}
.feature-card .pic{height:226px}
.feature-card .cap{position:absolute;left:0;bottom:0;width:100%;height:64px;background:rgba(30,30,30,.85);color:var(--white);padding:10px 0 0 66px}
.feature-card .cap b{display:block;font-family:var(--serif);font-size:15px;font-weight:400}
.feature-card .cap span{font-size:11px;color:#ccc}
.feature-card .cap svg{position:absolute;left:20px;top:16px}

/* section heads */
.eyebrow-sm{width:1200px;text-align:center;font-size:13px;letter-spacing:1.5px;color:#444}
.sec-title{width:1200px;text-align:center;font-family:var(--serif);font-weight:700;font-size:34px;color:var(--ink)}

/* services */
.service{width:240px;text-align:center;top:1110px}
.service svg{display:block;margin:0 auto}
.service h3{margin-top:28px;font-family:var(--serif);font-weight:400;font-size:20px;color:var(--blue)}
.service p{margin-top:22px;font-size:16px;line-height:25px;color:#333}
.more{left:486px;top:1414px;width:228px;height:50px;font-size:17px}

/* stats */
.stats{left:0;top:1569px;width:1200px;height:296px;background:linear-gradient(100deg,#2a3440 0%,#4b4a48 45%,#2c3846 100%)}
.stat{top:1660px;width:260px;text-align:center;color:var(--white)}
.stat svg{display:block;margin:0 auto}
.stat strong{display:block;margin-top:8px;font-size:32px;font-weight:600}
.stat span{display:block;margin-top:6px;font-size:15px}

/* locations */
.loc-frame{left:353px;top:2080px;width:434px;height:437px;border:3px solid #ccc}
.loc{width:494px;overflow:hidden;box-shadow:0 3px 10px rgba(0,0,0,.2)}
.loc .cap{position:absolute;left:0;bottom:0;width:100%;height:120px;background:rgba(25,25,25,.8);color:var(--white);padding:26px 28px}
.loc .cap h3{font-size:28px;font-weight:700}
.loc .cap p{margin-top:10px;font-size:15px;line-height:21px;width:380px}

/* video */
.video{left:0;top:2642px;width:1200px;height:562px;background:linear-gradient(180deg,#1c2229 0%,#2f3a44 55%,#3a4650 100%)}
.video .play{position:absolute;left:541px;top:226px}
.video .controls{position:absolute;left:0;bottom:0;width:100%;height:76px;background:rgba(0,0,0,.35)}

/* contact */
.contact{left:0;top:3204px;width:1200px;height:611px;background:var(--contact-bg)}
.contact-brand{left:66px;top:3358px;display:flex;align-items:center;gap:10px;font-weight:700;font-size:34px;color:var(--blue)}
.contact-brand .sq{width:14px;height:14px;background:var(--blue)}
.addr{left:66px;font-size:20px;color:#222}
.addr-socials{left:288px;top:3486px;display:flex;gap:26px}
.addr-socials .dot{background:var(--blue)}
.mail{left:66px;font-size:15px;color:#666}
.updates-title{left:643px;top:3358px;width:443px;text-align:center;font-size:30px;color:#333;display:flex;justify-content:center;gap:8px;align-items:flex-start}
.updates-sub{left:600px;top:3406px;width:530px;text-align:center;font-size:14px;color:#666}
.field{height:38px;background:var(--white);border:1px solid #bbb;font-size:14px;color:#444;padding:9px 10px}
.submit{left:768px;top:3698px;width:174px;height:50px;border-radius:25px;font-size:15px}

/* partners */
.partners{left:0;top:3815px;width:1200px;height:176px;background:var(--grey-band)}
.badge{top:3870px;height:72px;background:#fff;border:2px solid var(--blue-pale)}

/* footer */
.footer{left:0;top:3991px;width:1200px;height:81px;background:var(--blue);color:var(--white);font-size:14px}
.footer ul{position:absolute;left:66px;top:31px;list-style:none;display:flex;gap:26px}
.footer small{position:absolute;right:66px;top:33px;font-size:13px}
</style>
</head>
<body>

<header class="abs topbar">
  <span class="tagline">Transportation, Distribution &amp; Warehousing Inc.</span>
  <span class="phone">
    <svg width="12" height="18" viewBox="0 0 12 18"><rect x="1" y="1" width="10" height="16" rx="2" fill="none" stroke="#fff" stroke-width="2"/><circle cx="6" cy="14" r="1.2" fill="#fff"/></svg>
    555-210-4800
  </span>
  <span class="socials"><i class="dot"></i><i class="dot"></i><i class="dot"></i></span>
</header>

<nav class="abs nav">
  <div class="brand"><i class="sq"></i>Brightlane</div>
  <ul><li>What We Do</li><li>How We Do It</li><li>Who We Are</li><li>Tracking</li><li>Chat</li><li>Contact</li></ul>
  <div class="login">LOG IN</div>
</nav>

<section class="abs hero" role="img" aria-label="Long-exposure photo of railway tracks with streaking lights at sunset">
  <p class="eyebrow">WELCOME TO BRIGHTLANE</p>
  <h1>RELAX, WE GOT THIS</h1>
  <a class="btn">GET STARTED NOW</a>
</section>

<div class="abs feature-band"></div>
<article class="abs feature-card" style="left:155px">
  <div class="pic" role="img" aria-label="Cargo port cranes and containers at dusk" style="background:linear-gradient(180deg,#5b4a7a,#c4705a 60%,#2c3e55)"></div>
  <div class="cap"><svg width="26" height="26" viewBox="0 0 26 26"><rect x="3" y="8" width="20" height="14" fill="none" stroke="#fff" stroke-width="2"/><path d="M3 8l10-5 10 5" fill="none" stroke="#fff" stroke-width="2"/></svg><b>Cargo</b><span>Fast Shipment</span></div>
</article>
<article class="abs feature-card" style="left:475px">
  <div class="pic" role="img" aria-label="Front view of a passenger jet on the runway" style="background:linear-gradient(180deg,#e2a664,#d8c8a8 55%,#8a8578)"></div>
  <div class="cap"><svg width="26" height="26" viewBox="0 0 26 26"><path d="M3 23L23 3M8 6l12 2M18 6l2 12M5 16l5 5" fill="none" stroke="#fff" stroke-width="2"/></svg><b>International</b><span>Fast Shipment</span></div>
</article>
<article class="abs feature-card" style="left:795px">
  <div class="pic" role="img" aria-label="Portrait of a company professional" style="background:linear-gradient(180deg,#e8e8e8,#b9b9b9)"></div>
  <div class="cap"><svg width="26" height="26" viewBox="0 0 26 26"><path d="M3 13l10-10 10 10-10 10z" fill="none" stroke="#fff" stroke-width="2"/></svg><b>PROFESSIONAL</b><span>Fast Shipment</span></div>
</article>

<p class="abs eyebrow-sm" style="top:975px;left:0;font-size:11px">WHAT WE DO</p>
<h2 class="abs sec-title" style="top:1000px;left:0">Our Services</h2>

<div class="abs service" style="left:75px">
  <svg width="64" height="64" viewBox="0 0 64 64"><path d="M10 54L54 10M20 16l28 4M44 16l4 28M14 40l10 10" fill="none" stroke="#0355a3" stroke-width="4" stroke-linecap="round"/></svg>
  <h3>Air Fright</h3>
  <p>Lorem ipsum dolor sit amet, consectetur adip scing elit sed do.</p>
</div>
<div class="abs service" style="left:347px">
  <svg width="90" height="64" viewBox="0 0 90 64"><rect x="4" y="12" width="50" height="34" fill="none" stroke="#0355a3" stroke-width="3"/><path d="M54 22h18l12 12v12H54z" fill="none" stroke="#0355a3" stroke-width="3"/><circle cx="20" cy="50" r="6" fill="#fff" stroke="#0355a3" stroke-width="3"/><circle cx="70" cy="50" r="6" fill="#fff" stroke="#0355a3" stroke-width="3"/></svg>
  <h3>Car Fright</h3>
  <p>Lorem ipsum dolor sit amet, consectetur adip scing elit sed do.</p>
</div>
<div class="abs service" style="left:624px">
  <svg width="70" height="64" viewBox="0 0 70 64"><path d="M6 38h58l-8 16H14z" fill="none" stroke="#0355a3" stroke-width="3"/><rect x="18" y="20" width="34" height="18" fill="none" stroke="#0355a3" stroke-width="3"/><rect x="28" y="6" width="14" height="14" fill="none" stroke="#0355a3" stroke-width="3"/><path d="M4 60q8-5 16 0t16 0 16 0 16 0" fill="none" stroke="#0355a3" stroke-width="3"/></svg>
  <h3>Ship Fright</h3>
  <p>Lorem ipsum dolor sit amet, consectetur adip scing elit sed do.</p>
</div>
<div class="abs service" style="left:898px">
  <svg width="56" height="64" viewBox="0 0 56 64"><rect x="8" y="4" width="40" height="46" rx="8" fill="none" stroke="#0355a3" stroke-width="3"/><rect x="15" y="12" width="26" height="16" fill="none" stroke="#0355a3" stroke-width="3"/><circle cx="18" cy="39" r="3" fill="#0355a3"/><circle cx="38" cy="39" r="3" fill="#0355a3"/><path d="M16 50l-8 12M40 50l8 12" stroke="#0355a3" stroke-width="3"/></svg>
  <h3>Train Fright</h3>
  <p>Lorem ipsum dolor sit amet, consectetur adip scing elit sed do.</p>
</div>
<a class="abs btn more">More Services</a>

<section class="abs stats" role="img" aria-label="Dusk photo of a cargo ship bow beside harbour cranes"></section>
<div class="abs stat" style="left:38px">
  <svg width="48" height="48" viewBox="0 0 48 48"><circle cx="24" cy="24" r="20" fill="none" stroke="#fff" stroke-width="2"/><ellipse cx="24" cy="24" rx="9" ry="20" fill="none" stroke="#fff" stroke-width="2"/><path d="M4 24h40M8 14h32M8 34h32" stroke="#fff" stroke-width="2"/></svg>
  <strong>250</strong><span>Service Centre</span>
</div>
<div class="abs stat" style="left:332px">
  <svg width="48" height="48" viewBox="0 0 48 48"><circle cx="24" cy="16" r="9" fill="none" stroke="#fff" stroke-width="2"/><path d="M8 46c0-12 7-18 16-18s16 6 16 18" fill="none" stroke="#fff" stroke-width="2"/></svg>
  <strong>1350</strong><span>Company With Employee</span>
</div>
<div class="abs stat" style="left:603px">
  <svg width="48" height="48" viewBox="0 0 48 48"><circle cx="24" cy="24" r="20" fill="none" stroke="#fff" stroke-width="2"/><circle cx="17" cy="19" r="2" fill="#fff"/><circle cx="31" cy="19" r="2" fill="#fff"/><path d="M15 29q9 9 18 0" fill="none" stroke="#fff" stroke-width="2"/></svg>
  <strong>2,00,000+</strong><span>Happy customers</span>
</div>
<div class="abs stat" style="left:888px">
  <svg width="48" height="48" viewBox="0 0 48 48"><path d="M8 30V24a16 16 0 0132 0v6" fill="none" stroke="#fff" stroke-width="2"/><rect x="4" y="26" width="8" height="12" rx="2" fill="none" stroke="#fff" stroke-width="2"/><rect x="36" y="26" width="8" height="12" rx="2" fill="none" stroke="#fff" stroke-width="2"/><path d="M40 38q0 6-12 6" fill="none" stroke="#fff" stroke-width="2"/></svg>
  <strong>24/7</strong><span>Service Centre Support</span>
</div>

<p class="abs eyebrow-sm" style="top:1914px;left:0">OUR</p>
<h2 class="abs sec-title" style="top:1940px;left:0;font-size:30px">Locations</h2>

<div class="abs loc-frame"></div>
<article class="abs loc" style="left:92px;top:2039px;height:434px" >
  <div role="img" aria-label="Chicago skyline at sunset" style="height:100%;background:linear-gradient(180deg,#4a5d8a 0%,#c07a6a 40%,#e0965a 55%,#2b2f3a 100%)"></div>
  <div class="cap"><h3>Chicago</h3><p>Contrary to popular belief, Lorem Ipsum is not simply random text. It has roots in a piece</p></div>
</article>
<article class="abs loc" style="left:630px;top:2120px;height:438px">
  <div role="img" aria-label="Palatine landmark under a blue sky" style="height:100%;background:linear-gradient(180deg,#8fb6dc 0%,#c9d8e6 35%,#b79c7c 60%,#5c6b44 100%)"></div>
  <div class="cap"><h3>Palatine</h3><p>Contrary to popular belief, Lorem Ipsum is not simply random text. It has roots in a piece</p></div>
</article>

<section class="abs video" role="img" aria-label="Video still of a container terminal with cranes at dusk">
  <svg class="play" width="112" height="112" viewBox="0 0 112 112"><circle cx="56" cy="56" r="52" fill="none" stroke="#fff" stroke-width="5"/><path d="M45 34l32 22-32 22z" fill="#fff"/></svg>
  <div class="controls">
    <svg style="position:absolute;left:510px;top:28px" width="180" height="20" viewBox="0 0 180 20"><rect x="0" y="3" width="3" height="14" fill="#fff"/><path d="M14 3L4 10l10 7z" fill="#fff"/><path d="M78 2l14 8-14 8z" fill="#fff"/><path d="M148 3l10 7-10 7z" fill="#fff"/><rect x="158" y="3" width="3" height="14" fill="#fff"/></svg>
    <svg style="position:absolute;left:800px;top:30px" width="20" height="16" viewBox="0 0 20 16"><path d="M1 5h4l5-4v14l-5-4H1z" fill="#fff"/><path d="M13 4q4 4 0 8" fill="none" stroke="#fff" stroke-width="2"/></svg>
  </div>
</section>

<section class="abs contact"></section>
<p class="abs eyebrow-sm" style="top:3266px;left:0;font-size:11px">OUR</p>
<h2 class="abs sec-title" style="top:3290px;left:0;font-size:30px">Contact us</h2>

<div class="abs contact-brand"><i class="sq"></i>Brightlane</div>
<p class="abs addr" style="top:3428px">418 W Orchard Ave&nbsp; Suite 7</p>
<p class="abs addr" style="top:3466px">Palatine, IL&nbsp;&nbsp; 60099</p>
<div class="abs addr-socials"><i class="dot"></i><i class="dot"></i><i class="dot"></i></div>
<p class="abs addr" style="top:3534px">Office Phone: 555-210-4800</p>
<p class="abs addr" style="top:3571px">Warehouse: 555-210-4802</p>
<p class="abs addr" style="top:3607px">Fax: 555-210-4801</p>
<p class="abs mail" style="top:3656px">Rates: rates@brightlanefreight.com</p>
<p class="abs mail" style="top:3692px">Warehouse: warehouse@brightlanefreight.com</p>
<p class="abs mail" style="top:3728px">Information: info@brightlanefreight.com</p>

<h3 class="abs updates-title" style="font-weight:400">Get Updates
  <svg width="16" height="14" viewBox="0 0 16 14" style="margin-top:6px"><rect x="1" y="1" width="14" height="12" fill="none" stroke="#0355a3" stroke-width="1.5"/><path d="M1 1l7 6 7-6" fill="none" stroke="#0355a3" stroke-width="1.5"/></svg>
</h3>
<p class="abs updates-sub">Sign up and we promise to deliver quality information to you.</p>
<div class="abs field" style="left:643px;top:3455px;width:210px">First Name</div>
<div class="abs field" style="left:869px;top:3455px;width:217px">Last Name</div>
<div class="abs field" style="left:643px;top:3544px;width:443px">Organisation</div>
<div class="abs field" style="left:643px;top:3617px;width:443px">E-mail</div>
<a class="abs btn submit">SUBMIT</a>

<section class="abs partners"></section>
<div class="abs badge" style="left:66px;width:164px;border-radius:10px" role="img" aria-label="Certification badge"></div>
<div class="abs badge" style="left:285px;width:142px" role="img" aria-label="Award badge"></div>
<div class="abs badge" style="left:502px;width:144px;border-color:transparent;background:transparent" role="img" aria-label="Partner badge"><svg width="144" height="72"><ellipse cx="72" cy="36" rx="68" ry="24" fill="#fff" stroke="#c9b6dc" stroke-width="2"/></svg></div>
<div class="abs badge" style="left:700px;width:236px" role="img" aria-label="Business ethics award badge"></div>
<div class="abs badge" style="left:956px;width:170px;height:96px;top:3856px" role="img" aria-label="Business award badge"></div>

<footer class="abs footer">
  <ul><li>What We Do</li><li>How We Do It</li><li>Who We Are</li><li>Tracking</li><li>Chat</li><li>Contact</li></ul>
  <small>© 2017 All Right Reserved</small>
</footer>

</body>
</html>
```